Hair and Wellness Brochure and Pricelist design

I am requiring a brochure that has a fresh, though alternative design. My business name is The Quiet Harbour Hair and Wellness. I have a very professional approach to my work and love to give that little bit extra to all of my clients. My passion for health, has led me to channel my business alternatively by using non toxic colours and styling products and through that same vein, I have studied Aromatherapy, Indian Head Massage and Reiki...all additional services I use where required.
My studio has very neutral tones of beige,white and beech wood but these tones aren't necessarily required for the brochure.I like to create a space of calm, peace and quiet, where my clients feel refreshed and rejuvenated..

Industry/Entity Type

Business

```html
<!DOCTYPE html>
<html lang="en">
<head>
<meta charset="utf-8">
<title>The Quiet Harbour Hair and Wellness – Price List</title>
<link href="https://fonts.googleapis.com/css2?family=Barlow:wght@500;600;700&display=swap" rel="stylesheet">
<style>
  :root {
    --page: #ffffff;
    --wood-light: #d9ad98;
    --wood-mid: #cf9f88;
    --wood-dark: #c28f78;
    --band: rgba(246, 232, 226, 0.72);
    --ink: #2b1d19;
    --green-light: #8cc63f;
    --green-dark: #5ea040;
    --white: #ffffff;
    --fold: rgba(60, 40, 35, 0.55);
  }
  * { box-sizing: border-box; margin: 0; padding: 0; }
  html, body { width: 1200px; height: 1000px; overflow: hidden; background: var(--page); }
  body { font-family: "Barlow", "Helvetica Neue", Arial, sans-serif; color: var(--ink); }

  .canvas { position: relative; width: 1200px; height: 1000px; }

  .brochure {
    position: absolute; left: 117px; top: 125px; width: 966px; height: 750px; overflow: hidden;
  }
  .wood-surface {
    position: absolute; inset: 0;
    background:
      linear-gradient(180deg, rgba(255,255,255,0.10) 0 8%, transparent 8% 21%, rgba(255,255,255,0.08) 21% 34%, transparent 34% 47%, rgba(120,70,50,0.05) 47% 60%, transparent 60% 73%, rgba(255,255,255,0.06) 73% 86%, transparent 86%),
      linear-gradient(90deg, var(--wood-light), var(--wood-mid) 45%, var(--wood-dark));
  }
  .band { position: absolute; left: 0; background: var(--band); }
  .band--title { top: 111px; height: 41px; width: 822px;
    clip-path: polygon(0 0, 36px 0, 30px 50%, 36px 100%, 0 100%); }
  .band--title-right { position: absolute; top: 111px; left: 279px; height: 41px; width: 545px; background: var(--band);
    clip-path: polygon(8px 0, 100% 0, 100% 100%, 8px 100%, 0 50%); }
  .band--logo { top: 557px; height: 103px; width: 966px; }

  .fold { position: absolute; top: 0; bottom: 0; border-left: 1px dashed var(--fold); }
  .fold--one { left: 321px; }
  .fold--two { left: 641px; }

  .foliage, .orchids { position: absolute; }
  .foliage { right: 0; top: 0; width: 410px; height: 300px; }
  .orchids { right: 0; top: 190px; width: 740px; height: 560px; }

  .ribbon {
    position: absolute; left: 43px; top: 112px; width: 229px; height: 38px;
    background: linear-gradient(90deg, var(--green-light), var(--green-dark));
    clip-path: polygon(0 0, 100% 0, 96% 50%, 100% 100%, 0 100%, 4% 50%);
    display: flex; align-items: center; justify-content: center;
  }
  .ribbon::before { content: ""; position: absolute; left: 10px; right: 10px; top: 3px; bottom: 3px;
    border-top: 1px dashed rgba(255,255,255,0.8); border-bottom: 1px dashed rgba(255,255,255,0.8); }
  .ribbon__title { color: var(--white); font-weight: 700; font-size: 19px; letter-spacing: 0.5px; }

  .tagline { position: absolute; left: 381px; top: 117px; font-weight: 600; font-size: 12px; line-height: 15px; }

  .price-column { position: absolute; width: 206px; }
  .price-column--left { left: 61px; top: 189px; }
  .price-column--middle { left: 381px; top: 189px; }

  .section + .section { margin-top: 20px; }
  .section--spaced + .section--spaced { margin-top: 19px; }
  .section__heading { font-weight: 700; font-size: 14.5px; line-height: 18px; letter-spacing: 0.3px; margin-bottom: 2px; }

  .item { font-weight: 600; font-size: 11.5px; line-height: 15px; margin-bottom: 4.5px; }
  .item__line { display: flex; align-items: baseline; }
  .item__leader { flex: 1; border-bottom: 2px dotted var(--ink); margin: 0 4px; transform: translateY(-3px); opacity: 0.8; }
  .item__price { font-weight: 700; }
  .item__note { display: block; }

  .brand-name {
    position: absolute; left: 61px; top: 586px; width: 240px;
    display: flex; align-items: center; gap: 10px;
  }
  .brand-name__dot { flex: none; width: 14px; height: 14px; border-radius: 50%; background: var(--green-dark); }
  .brand-name__text { color: var(--ink); font-weight: 700; font-size: 15px; line-height: 20px; letter-spacing: 0.3px; }
</style>
</head>
<body>
<div class="canvas">
  <section class="brochure">
    <div class="wood-surface" role="img" aria-label="Light beech wood plank background"></div>

    <svg class="foliage" viewBox="0 0 410 300" role="img" aria-label="Fresh green fern leaves in the top right corner">
      <defs>
        <radialGradient id="leafTone" cx="75%" cy="20%" r="80%">
          <stop offset="0" stop-color="#5c9a2a"/>
          <stop offset="0.55" stop-color="#a6cf48" stop-opacity="0.85"/>
          <stop offset="1" stop-color="#d6e88a" stop-opacity="0"/>
        </radialGradient>
      </defs>
      <path d="M0 0 H410 V300 C340 260 300 220 250 170 C180 110 80 60 0 0 Z" fill="url(#leafTone)"/>
    </svg>

    <svg class="orchids" viewBox="0 0 740 560" role="img" aria-label="White orchid blossoms on green stems along the right and bottom edges">
      <defs>
        <radialGradient id="bloomTone" cx="80%" cy="75%" r="75%">
          <stop offset="0" stop-color="#f7f5ef"/>
          <stop offset="0.6" stop-color="#ede9df"/>
          <stop offset="1" stop-color="#e6e1d5" stop-opacity="0.9"/>
        </radialGradient>
      </defs>
      <path d="M740 0 V560 H0 C10 520 40 470 90 455 C160 440 230 470 290 440 C320 380 330 330 400 320 C470 300 520 250 560 230 C600 180 580 120 620 70 C650 30 700 10 740 0 Z" fill="url(#bloomTone)"/>
    </svg>

    <div class="band band--title"></div>
    <div class="band--title-right"></div>
    <div class="band band--logo"></div>

    <div class="fold fold--one"></div>
    <div class="fold fold--two"></div>

    <div class="ribbon"><h1 class="ribbon__title">PRICE LIST</h1></div>

    <p class="tagline">All services include a soothing<br>aromatherapy neck massage</p>

    <div class="price-column price-column--left">
      <div class="section">
        <h2 class="section__heading">CUTS</h2>
        <p class="item"><span class="item__line">Shampoo &amp; blow dry<span class="item__leader"></span><span class="item__price">$40</span></span></p>
        <p class="item">Hot tool styling with Shampoo<span class="item__line">included<span class="item__leader"></span><span class="item__price">$50</span></span></p>
        <p class="item"><span class="item__line">Shampoo cut &amp; blow dry<span class="item__leader"></span><span class="item__price">$70</span></span></p>
        <p class="item"><span class="item__line">Men’s style cut<span class="item__leader"></span><span class="item__price">$30</span></span></p>
      </div>
      <div class="section">
        <h2 class="section__heading">COLOUR</h2>
        <p class="item">Tint &amp; semi permanent<span class="item__line">regrowth colour<span class="item__leader"></span><span class="item__price">$60</span></span></p>
        <p class="item"><span class="item__line">Half head foils<span class="item__leader"></span><span class="item__price">$60</span></span></p>
        <p class="item"><span class="item__line">Full head foils<span class="item__leader"></span><span class="item__price">$120</span></span></p>
        <p class="item">Any additional colour<span class="item__line">starts from<span class="item__leader"></span><span class="item__price">$30</span></span></p>
        <p class="item">Corrective colour services are priced<br>at consultation</p>
      </div>
    </div>

    <div class="price-column price-column--middle">
      <div class="section section--spaced">
        <h2 class="section__heading">OTHER SERVICES</h2>
        <p class="item">45 minute Indian Head Massage<br>with a Reiki and<span class="item__line">Aromatherapy Infusion<span class="item__leader"></span><span class="item__price">$50</span></span></p>
      </div>
      <div class="section section--spaced">
        <h2 class="section__heading">WEDDING AND FORMAL<br>CONSULTATIONS</h2>
        <p class="item">Hair up styling including<span class="item__line">the use of hot tools<span class="item__leader"></span><span class="item__price">$50</span></span></p>
        <p class="item">All wedding hairstyling<span class="item__line">starts from<span class="item__leader"></span><span class="item__price">$60</span></span><span class="item__note">(Price on consultation)</span></p>
        <p class="item"><span class="item__line">Wedding up style consultation<span class="item__leader"></span><span class="item__price">$50</span></span></p>
      </div>
    </div>

    <div class="brand-name">
      <span class="brand-name__dot"></span>
      <p class="brand-name__text">The Quiet Harbour<br>Hair and Wellness</p>
    </div>
  </section>
</div>
</body>
</html>
```